New Design for Water Vending Machine

Re-design graphics for face plate of water jug vending machine.

Attached are the following:
-Picture of the current face plate for the vending machine. The layout and workflow of the system have been changed.
-Picture of the new face plate without a decal installed.
-Picture of an actual installation of these vending machines for reference.
-DXF File with layout of the face plate
-PDF File with layout notes

The graphics will be printed on a lexan decal. There will be holes cutout for the following:
-Corvel Credit card reader
-Coin reject button
-Coin slot
-4 x Buttons
-Change return
Each of the cutouts should be approximately 5mm larger in all directions than the cutout size on the DXF file.

The flow of the system is as follows:
1. Insert Coins or tap Pendra/Credit/PrePaid Card
2. Press 'Format' button until desired bottle size is displayed.
3. Press 'Start' to begin filling.
'Pause' Button may be pressed during fill to switch containers or temporarily pause fill.
A poster has also been attached that is currently displayed above the prototype machines for customer reference.

Note that the bottom button is not currently used. Perhaps the design could include a window of sorts to add a label to it down the road.

The logos for TallyCoin, Orbu and Pendra Zip could be displayed near the cutout for the Corvel system.

The phrase 'Premium Drinking Water processed by Reverse Osmosis' should be displayed somewhere on the plate.

Dimensions of the face plate are 12.75" wide x 29.75" high. Dimensions of the graphics will be 10.25" x 27".

The display window will simply be clear lexan. No material will be cutout. Buffer space around display window should be 7mm.

Requirements
Must have
• Vibrant colors, and be eye catching. We want customers to be visually appealed by the machine. It should also follow a blue color theme. Text needs to be clearly layed out, and be concise.

```html
<!DOCTYPE html>
<html lang="en">
<head>
<meta charset="utf-8">
<title>Premium Drinking Water – Vending Face Plate</title>
<link rel="stylesheet" href="https://fonts.googleapis.com/css2?family=Arimo:ital,wght@0,400;0,700;1,700&display=swap">
<style>
  :root {
    --page: #ffffff;
    --blue-deep: #1c4fa0;
    --blue-mid: #1f78cf;
    --blue-bright: #2aa6ea;
    --band: rgba(24, 66, 150, 0.88);
    --white: #ffffff;
    --red-line: #d9262a;
    --ink-dark: #1f3a6e;
  }
  * { box-sizing: border-box; margin: 0; padding: 0; }
  html, body { width: 1200px; height: 1018px; overflow: hidden; background: var(--page); }
  body { position: relative; font-family: "Arimo", Arial, sans-serif; color: var(--white); }

  .install-view {
    position: absolute; left: 54px; top: 382px; width: 312px; height: 268px;
    background: linear-gradient(160deg, var(--blue-deep), var(--blue-bright) 55%, var(--blue-deep));
  }

  .plate {
    position: absolute; top: 46px; width: 347px; height: 916px;
    border-radius: 4px; overflow: hidden;
    background: linear-gradient(180deg, var(--blue-deep) 0%, var(--blue-mid) 25%, var(--blue-bright) 50%, var(--blue-mid) 75%, var(--blue-deep) 100%);
  }
  .plate--a { left: 399px; }
  .plate--b { left: 781px; }
  .plate > * { position: absolute; }

  .label-strip { left: 75px; top: 13px; width: 199px; height: 30px; background: var(--white); }

  .coin-icon { left: 82px; top: 96px; width: 44px; height: 54px; }

  .step-band {
    background: var(--band); display: flex; align-items: center;
  }
  .step-number { font-weight: 700; font-size: 38px; line-height: 1; }

  .step-one { left: 21px; top: 161px; width: 186px; height: 51px; padding-left: 9px; gap: 8px; }
  .step-one .step-number { font-size: 40px; }
  .step-one-title { font-size: 9px; line-height: 1.15; }
  .step-one-note { font-size: 7px; font-weight: 700; line-height: 1.2; margin-top: 3px; }

  .clear-window {
    background: var(--white); border-radius: 8px; padding: 6px;
  }
  .clear-window span { display: block; width: 100%; height: 100%; border: 1.5px solid var(--red-line); }
  .display-window { left: 216px; top: 94px; width: 126px; height: 153px; }
  .change-window { left: 22px; top: 801px; width: 120px; height: 63px; }

  .card-panel {
    left: 215px; top: 253px; width: 127px; height: 46px; background: var(--band);
    text-align: center; padding-top: 5px; border-radius: 3px;
  }
  .card-row { display: flex; justify-content: center; gap: 2px; }
  .card-chip {
    background: var(--white); color: var(--ink-dark); font-size: 5px; font-weight: 700;
    padding: 3px 2px; border-radius: 1px; white-space: nowrap;
  }
  .card-note { font-size: 6.5px; font-weight: 700; line-height: 1.25; margin-top: 5px; }

  .button-row { left: 122px; width: 188px; height: 51px; justify-content: flex-end; padding-right: 60px; }
  .button-row .step-number { position: absolute; left: 12px; top: 7px; }
  .button-title { font-size: 16px; font-weight: 700; text-align: right; }
  .button-hint { font-size: 7px; font-weight: 700; text-align: right; line-height: 1.2; }
  .row-format { top: 337px; }
  .row-format .button-title { font-size: 16px; }
  .row-start { top: 439px; }
  .row-pause { top: 541px; }
  .row-spare { top: 642px; }

  .push-button {
    left: 256px; width: 46px; height: 46px; border-radius: 50%;
    background: var(--white); display: flex; align-items: center; justify-content: center;
  }
  .push-button::after {
    content: ""; width: 38px; height: 38px; border-radius: 50%; border: 1.5px solid var(--red-line);
  }
  .btn-format { top: 340px; }
  .btn-start { top: 442px; }
  .btn-pause { top: 543px; }
  .btn-spare { top: 644px; }

  .tagline { left: 0; width: 100%; text-align: center; font-style: italic; font-weight: 700; }
  .tagline-main { top: 724px; font-size: 24px; }
  .tagline-sub { top: 758px; font-size: 16.5px; }
</style>
</head>
<body>

<div class="install-view" role="img" aria-label="Photo of the installed vending machines on a blue water-drop wall"></div>

<section class="plate plate--a">
  <div class="label-strip"></div>
  <svg class="coin-icon" viewBox="0 0 44 54" aria-hidden="true">
    <circle cx="12" cy="26" r="11" fill="#fff"/>
    <circle cx="12" cy="26" r="6.5" fill="none" stroke="#d9262a" stroke-width="1.3"/>
    <rect x="27" y="0" width="15" height="54" rx="7.5" fill="#fff"/>
    <rect x="32.5" y="5" width="4" height="44" rx="2" fill="none" stroke="#d9262a" stroke-width="1.3"/>
  </svg>
  <div class="step-band step-one">
    <span class="step-number">1</span>
    <div>
      <p class="step-one-title">Insert Coins or tap<br>Pendra/Credit/PrePaid Card</p>
      <p class="step-one-note">Machine will provide change when bottle<br>size is selected, and start button is pressed</p>
    </div>
  </div>
  <div class="clear-window display-window"><span></span></div>
  <div class="card-panel">
    <div class="card-row">
      <span class="card-chip">TallyCoin</span><span class="card-chip">Orbu</span><span class="card-chip">Pendra</span><span class="card-chip">Pendra Zip</span>
    </div>
    <p class="card-note">Credit/Pendra and coin<br>combinations not accepted</p>
  </div>
  <div class="step-band button-row row-format">
    <span class="step-number">2</span>
    <div><p class="button-title">Format</p><p class="button-hint">Press until desired<br>bottle size is displayed</p></div>
  </div>
  <div class="push-button btn-format"></div>
  <div class="step-band button-row row-start">
    <span class="step-number">3</span>
    <p class="button-title">Start</p>
  </div>
  <div class="push-button btn-start"></div>
  <div class="step-band button-row row-pause"><p class="button-title">Pause</p></div>
  <div class="push-button btn-pause"></div>
  <div class="step-band button-row row-spare"></div>
  <div class="push-button btn-spare"></div>
  <p class="tagline tagline-main">Premium Drinking Water</p>
  <p class="tagline tagline-sub">Processed by Reverse Osmosis</p>
  <div class="clear-window change-window"><span></span></div>
</section>

<section class="plate plate--b">
  <div class="label-strip"></div>
  <svg class="coin-icon" viewBox="0 0 44 54" aria-hidden="true">
    <circle cx="12" cy="26" r="11" fill="#fff"/>
    <circle cx="12" cy="26" r="6.5" fill="none" stroke="#d9262a" stroke-width="1.3"/>
    <rect x="27" y="0" width="15" height="54" rx="7.5" fill="#fff"/>
    <rect x="32.5" y="5" width="4" height="44" rx="2" fill="none" stroke="#d9262a" stroke-width="1.3"/>
  </svg>
  <div class="step-band step-one">
    <span class="step-number">1</span>
    <div>
      <p class="step-one-title">Insert Coins or tap<br>Pendra/Credit/PrePaid Card</p>
      <p class="step-one-note">Machine will provide change when bottle<br>size is selected, and start button is pressed</p>
    </div>
  </div>
  <div class="clear-window display-window"><span></span></div>
  <div class="card-panel">
    <div class="card-row">
      <span class="card-chip">TallyCoin</span><span class="card-chip">Orbu</span><span class="card-chip">Pendra</span><span class="card-chip">Pendra Zip</span>
    </div>
    <p class="card-note">Credit/Pendra and coin<br>combinations not accepted</p>
  </div>
  <div class="step-band button-row row-format">
    <span class="step-number">2</span>
    <div><p class="button-title">Format</p><p class="button-hint">Press until desired<br>bottle size is displayed</p></div>
  </div>
  <div class="push-button btn-format"></div>
  <div class="step-band button-row row-start">
    <span class="step-number">3</span>
    <p class="button-title">Start</p>
  </div>
  <div class="push-button btn-start"></div>
  <div class="step-band button-row row-pause"><p class="button-title">Pause</p></div>
  <div class="push-button btn-pause"></div>
  <div class="push-button btn-spare"></div>
  <p class="tagline tagline-main">Premium Drinking Water</p>
  <p class="tagline tagline-sub">Processed by Reverse Osmosis</p>
  <div class="clear-window change-window"><span></span></div>
</section>

</body>
</html>
```